Stationary and Business Card Design

We need a stationery design and a business card design for a non-profit economics development agency. Our website is brightledgerhub.org. Our clients are Canadian government agencies and large Chinese company. We need the design to be professional and corporate.

Please see attached for our Power Point presentation. Please take design elements from our website and our ppt.

```html
<!DOCTYPE html>
<html lang="en">
<head>
<meta charset="utf-8">
<title>Bright Ledger Alliance — Letterhead</title>
<link rel="stylesheet" href="https://fonts.googleapis.com/css2?family=Open+Sans:wght@400;700&display=swap">
<style>
  :root {
    --brand-red: #e3212d;
    --ink: #111111;
    --band: #000000;
    --paper: #ffffff;
  }
  html, body {
    margin: 0;
    padding: 0;
    overflow: hidden;
    background: var(--paper);
  }
  .letterhead {
    position: relative;
    width: 927px;
    height: 1200px;
    background: var(--paper);
    overflow: hidden;
    font-family: "Open Sans", Arial, sans-serif;
    color: var(--ink);
  }
  .header-band {
    position: absolute;
    left: 0;
    top: 0;
    width: 927px;
    height: 100px;
  }
  .brand-mark {
    position: absolute;
    left: 62px;
    top: 62px;
    margin: 0;
    font-size: 22px;
    font-weight: 700;
    line-height: 1;
    color: var(--brand-red);
    letter-spacing: 0.2px;
  }
  .org-name {
    position: absolute;
    left: 24px;
    top: 106px;
    margin: 0;
    font-size: 19px;
    font-weight: 700;
    line-height: 1;
    color: var(--ink);
  }
  .contact-line {
    position: absolute;
    top: 113px;
    margin: 0;
    font-family: Arial, "Open Sans", sans-serif;
    font-size: 11px;
    line-height: 1;
    color: var(--ink);
    white-space: nowrap;
  }
  .contact-address { left: 281px; }
  .contact-phone { left: 654px; }
  .contact-web { left: 776px; }
</style>
</head>
<body>
  <div class="letterhead">
    <svg class="header-band" viewBox="0 0 927 100" aria-hidden="true">
      <polygon fill="var(--band)" points="224,55 927,53 927,86 565,86 560,87 236,87"/>
    </svg>
    <p class="brand-mark">Bright Ledger</p>
    <p class="org-name">Bright Ledger Alliance</p>
    <p class="contact-line contact-address">2450 Harbourline Drive, Suite 410 Markham, Ontario L3R 5K2</p>
    <p class="contact-line contact-phone">PH | 416 555 0147</p>
    <p class="contact-line contact-web">www.brightledgerhub.org</p>
  </div>
</body>
</html>
```